LumaPeak business card

We are a performing arts company providing training (to both kids and adults) as well as performers for events. We hope to bring joy and confidence on stage to the people we train, as well as joy to the audience when our artistes perform. Designs should convey the joy, confidence and vibrancy on stage. Design business card using the attached logo. Card to include name, mobile tel, email address, company address, and website. Double sided. To also include the following list of what the company does:
• Training & Enrichment
• Private & Corporate Entertainment
- Music composition & production

Industry/Entity Type

Training

Contact Information for Business Card

Card to include name, mobile tel, email address, company address, and website. Double sided. To also include the following list of what the company does:
• Training & Enrichment

Requirements
Nice to have
• Card need not be the traditional rectangular in shape but not too outrageous.

```html
<!DOCTYPE html>
<html lang="en">
<head>
<meta charset="utf-8">
<title>LumaPeak business card</title>
<link rel="stylesheet" href="https://fonts.googleapis.com/css2?family=Exo+2:wght@400;500;600;700&display=swap">
<style>
  :root {
    --bg: #e6e2e2;
    --card-dark: #0b0b0b;
    --card-dark-edge: #1a1a1a;
    --card-light-center: #ffffff;
    --card-light-edge: #bdbdbd;
    --pink: #e8216f;
    --purple: #6d2c8e;
    --indigo: #2d2f7f;
    --blue: #1b8fd0;
    --green: #3aa54a;
    --yellow: #f6d21a;
    --orange: #f39019;
    --red: #e02634;
    --navy: #262a6b;
    --text-light: #e4e4e4;
    --brand: #e8216f;
  }
  * { box-sizing: border-box; margin: 0; padding: 0; }
  html, body { width: 1200px; height: 800px; overflow: hidden; }
  body {
    background: var(--bg);
    font-family: "Exo 2", sans-serif;
    position: relative;
  }
  .card {
    position: absolute;
    top: 245px;
    width: 540px;
    height: 310px;
    overflow: hidden;
  }
  .card--front { left: 40px; background: radial-gradient(circle at 50% 45%, var(--card-dark-edge), var(--card-dark) 75%); }
  .card--back  { left: 620px; background: radial-gradient(ellipse at 50% 40%, var(--card-light-center) 10%, var(--card-light-edge) 85%); }

  .rainbow-band { position: absolute; display: flex; }
  .rainbow-band span { flex: 1; }
  .rainbow-band--left { left: 0; top: 0; bottom: 0; width: 14px; flex-direction: column; }
  .rainbow-band--bottom { left: 0; right: 0; bottom: 0; height: 16px; flex-direction: row; }
  .c1 { background: var(--pink); } .c2 { background: var(--purple); }
  .c3 { background: var(--indigo); } .c4 { background: var(--blue); }
  .c5 { background: var(--green); } .c6 { background: var(--yellow); }
  .c7 { background: var(--orange); } .c8 { background: var(--red); }

  .brand-disc {
    position: absolute;
    left: 52px; top: 76px;
    width: 158px; height: 158px;
    border-radius: 50%;
    padding: 7px;
    background: conic-gradient(var(--red), var(--orange), var(--yellow), var(--green), var(--blue), var(--indigo), var(--purple), var(--pink), var(--red));
  }
  .brand-disc__inner {
    width: 100%; height: 100%;
    border-radius: 50%;
    background: #fff;
    display: flex; align-items: center; justify-content: center;
  }
  .brand-name { font-weight: 700; color: var(--brand); letter-spacing: 0.5px; white-space: nowrap; }
  .brand-disc .brand-name { font-size: 22px; }

  .divider {
    position: absolute;
    left: 250px; top: 60px;
    width: 3px; height: 190px;
    background: linear-gradient(to bottom, var(--red), var(--orange), var(--yellow), var(--green), var(--blue), var(--purple), var(--pink));
  }
  .contact { position: absolute; left: 282px; top: 96px; }
  .contact__name {
    font-size: 34px; font-weight: 500; letter-spacing: 1px; line-height: 1.2;
    background: linear-gradient(to right, var(--red), var(--orange), var(--yellow), var(--green), var(--blue), var(--purple), var(--pink));
    -webkit-background-clip: text; background-clip: text; color: transparent;
    margin-bottom: 14px;
  }
  .contact__list { list-style: none; }
  .contact__item {
    display: flex; align-items: center; gap: 10px;
    color: var(--text-light); font-size: 17px; line-height: 1.6; letter-spacing: 0.5px;
  }
  .contact__item svg { width: 13px; height: 13px; flex: none; }

  .brand-lockup {
    position: absolute; left: 0; right: 0; top: 88px;
    display: flex; align-items: center; justify-content: center; gap: 16px;
  }
  .brand-lockup .brand-name { font-size: 62px; line-height: 1.1; }
  .brand-mark-dot { width: 46px; height: 46px; border-radius: 50%; background: var(--blue); }
  .website {
    position: absolute; left: 0; right: 0; top: 200px;
    text-align: center; color: var(--navy);
    font-size: 19px; font-weight: 600; letter-spacing: 5px;
  }
</style>
</head>
<body>
  <section class="card card--front" aria-label="Card front">
    <div class="rainbow-band rainbow-band--left"><span class="c8"></span><span class="c7"></span><span class="c6"></span><span class="c5"></span><span class="c4"></span><span class="c3"></span><span class="c2"></span><span class="c1"></span></div>
    <div class="brand-disc"><div class="brand-disc__inner"><span class="brand-name">LumaPeak</span></div></div>
    <div class="divider"></div>
    <div class="contact">
      <p class="contact__name">Your Name</p>
      <ul class="contact__list">
        <li class="contact__item">
          <svg viewBox="0 0 12 12"><rect x="3" y="0.5" width="6" height="11" rx="1" fill="none" stroke="#e4e4e4" stroke-width="1.2"/></svg>
          mobile tel
        </li>
        <li class="contact__item">
          <svg viewBox="0 0 12 12"><rect x="0.6" y="2" width="10.8" height="8" fill="none" stroke="#e4e4e4" stroke-width="1.2"/><path d="M0.6 2 L6 6.5 L11.4 2" fill="none" stroke="#e4e4e4" stroke-width="1.2"/></svg>
          email address
        </li>
        <li class="contact__item">
          <svg viewBox="0 0 12 12"><path d="M6 11.5 C2.5 7 2 5.5 2 4.2 A4 4 0 0 1 10 4.2 C10 5.5 9.5 7 6 11.5 Z" fill="#e4e4e4"/><circle cx="6" cy="4.3" r="1.4" fill="#0b0b0b"/></svg>
          company address
        </li>
      </ul>
    </div>
  </section>

  <section class="card card--back" aria-label="Card back">
    <div class="brand-lockup">
      <span class="brand-mark-dot"></span>
      <span class="brand-name">LumaPeak</span>
    </div>
    <p class="website">YOURWEBSITE.COM</p>
    <div class="rainbow-band rainbow-band--bottom"><span class="c8"></span><span class="c7"></span><span class="c6"></span><span class="c5"></span><span class="c4"></span><span class="c3"></span><span class="c2"></span><span class="c1"></span></div>
  </section>
</body>
</html>
```